"Thank You" card for professional property management agency.

We need to create a DL size "Thank You" card primarily used to thank new clients for their business and referrals.
We are a real estate agency based on Sydney's Northern Beaches. We want the card to feel happy and professional, incorporating our logo.
See our website for details about our business - www.harbourleafrealty.com.au
We have attached our logo in black text and white text as well as some images we have used across our website.
One side must have the ability to hand write a message of thank you on.
I would like this to be a clean and simple design, feel free to use any image supplied, but we are also happy with plain or patterned designs too.

Target Market(s)

Property investors male and female aged 30-60

Industry/Entity Type

Real Estate

Font styles to use
Other font styles liked:
• Please let the designer choose font

Colors

Designer to choose colors to be used in the design.

Requirements
Must have
• DL Size: Full Bleed 213x102mm. Doc size 210x99mm (horizontal)
• Harbour Leaf Realty Logo
• Contact Details:
• info@harbourleafrealty.com.au
• Tel: 0498 217 603
• Level 2, 17 Wattlecombe Rd, Wattlecombe NSW 2187
• "Thank You" somewhere on the card
• Area or side to write message on.
• Design to be provided in editable photoshop PSD file and print ready PDF file
Nice to have
• Sleek professional design that feels "happy or grateful" as it is a thank you card
• Happy to use a plain colour or pattern on one side - it does not have to be an image provided, but feel free to design with either.
Should not have
• should not be too busy, keep it clean and simple.

```html
<!DOCTYPE html>
<html lang="en">
<head>
<meta charset="utf-8">
<title>Harbour Leaf Realty – Thank You Card</title>
<link href="https://fonts.googleapis.com/css2?family=Lato:wght@700;900&display=swap" rel="stylesheet">
<style>
  :root {
    --stage: #3a3a3c;
    --card: #f4fbfb;
    --card-tint: #e4f4f5;
    --ink: #1a1a1a;
    --text: #3a3a3a;
    --teal: #1f8f99;
    --rule: #222222;
    --sky: #2f8fc4;
    --sea: #1d7fb8;
    --foliage: #5d7a3a;
    --sand: #c9a46a;
  }
  * { box-sizing: border-box; margin: 0; padding: 0; }
  html, body {
    width: 1200px; height: 699px; overflow: hidden;
    background: var(--stage);
    font-family: "Lato", sans-serif;
  }
  .card {
    position: absolute; left: 46px; top: 89px;
    width: 1108px; height: 521px;
    background: var(--card);
    overflow: hidden;
  }
  .card-pattern {
    position: absolute; inset: 0;
    background: linear-gradient(135deg, var(--card) 0%, var(--card-tint) 50%, var(--card) 100%);
  }
  .thank-you {
    position: absolute; left: 31px; top: 96px;
    font-weight: 900; font-size: 40px; line-height: 1;
    color: var(--teal); white-space: nowrap;
  }
  .brand {
    position: absolute; right: 50px; top: 84px;
    font-weight: 900; font-size: 26px; line-height: 1;
    color: var(--ink); white-space: nowrap;
  }
  .gallery {
    position: absolute; left: 31px; top: 192px;
    width: 511px; height: 240px;
    display: grid; grid-template-columns: 1fr 1fr; grid-template-rows: 1fr 1fr;
  }
  .gallery .photo { width: 100%; height: 100%; }
  .photo-homes { background: linear-gradient(180deg, var(--sky) 0%, #8fb6c4 45%, var(--foliage) 100%); }
  .photo-beach { background: linear-gradient(180deg, #2a79b5 0%, #6a8a6e 50%, #2a8fbf 75%, #d9eef4 100%); }
  .photo-harbour { background: linear-gradient(180deg, #3a9ad4 0%, #4a7a54 30%, var(--sea) 45%, #0f5f98 100%); }
  .photo-tree { background: linear-gradient(180deg, #3f3a26 0%, #b9c4bf 45%, #8a6e44 70%, var(--sand) 100%); }
  .message-lines {
    position: absolute; left: 596px; top: 192px; width: 469px;
  }
  .message-lines span {
    position: absolute; left: 0; width: 100%;
    border-top: 2px solid var(--rule);
  }
  .contact {
    position: absolute; left: 32px; top: 472px;
    font-weight: 700; font-size: 20.5px; color: var(--text);
    white-space: nowrap;
  }
  .contact .sep { color: var(--teal); padding: 0 3px; }
</style>
</head>
<body>
  <main class="card">
    <div class="card-pattern" role="img" aria-label="Faint pale teal geometric line pattern covering the card"></div>

    <h1 class="thank-you">Thank You</h1>

    <div class="brand">HARBOUR LEAF REALTY</div>

    <div class="gallery">
      <div class="photo photo-homes" role="img" aria-label="Modern terraced homes with gardens under blue sky"></div>
      <div class="photo photo-beach" role="img" aria-label="Northern Beaches surf beach with headland and houses"></div>
      <div class="photo photo-harbour" role="img" aria-label="Boats moored on a blue harbour"></div>
      <div class="photo photo-tree" role="img" aria-label="Large fig tree framing a harbour beach at sunset"></div>
    </div>

    <div class="message-lines" aria-label="Lines for a handwritten message">
      <span style="top:0"></span>
      <span style="top:80px"></span>
      <span style="top:159px"></span>
      <span style="top:239px"></span>
    </div>

    <p class="contact">Level 2, 17 Wattlecombe Rd, Wattlecombe NSW 2187<span class="sep">|</span>Tel: 0498 217 603<span class="sep">|</span>Email: info@harbourleafrealty.com.au</p>
  </main>
</body>
</html>
```